Business Card Design, including supply of raw art files plus a vector diagram of the zelvon logo and

We need the business card design for a company that is launching a new exciting product. The brief requires the submission of the following once the final design is chosen:

- business card layout including raw files
- a composite vector image file of the zelvon logo and tag line
- a standalone vector image file of the zelvon logo

The product will be launched as a customer engagement app.

It has 4 core modules which enables a person to do multiple things - book tours and activities, order takeaways, search for local deals and offers. A universal currency is at the heart of this product. When you use the app, you earn cashback rewards when shopping or buying at any of the merchant partners across the modules as . These rewards can then be used as full or part payment when buying goods or services at these merchant partners.

The business card must help us build the brand, communicate the benefit of the brand's key focus - the ability to earn and burn this universal cashback ccurrency - across the 4 modules - booking of tours and activities, ordering, searching for local deals and payment.

We would like the design to use the brand's blue colour the hex colour is: 00
Dark grey : 646464
Darker blue shadow: 058bdd
Main Blue: 0084ff

We need to translate this into a CMYK print or spot colour print.

Both print options to be supplied as separate files.

An example of the base concept we have in mind is attached for your reference.

The font used by the brand is Proxima Nova.

Note: the duration has been set as 2 days.

Industry/Entity Type

Business

Contact Information for Business Card

Carla Mendoza
Marketing
W: www.zelvon.example
M: + 61 400555123
T: +61 2 5550 1473
A: Suite 7, Level 2, 14-18 Harwick Street, Sydney, NSW, 2000, Australia

Font styles to use
Sans Serif

Requirements
Must have
• zelVon logo and tagline
• address details
• zelVon icons as supplied
Nice to have
• would like to have the option of a spot varnish layer over the logo and icons at the back of the card

```html
<!DOCTYPE html>
<html lang="en">
<head>
<meta charset="utf-8">
<title>zelVon business card</title>
<link href="https://fonts.googleapis.com/css2?family=Montserrat:wght@300;400;600&display=swap" rel="stylesheet">
<style>
  :root {
    --backdrop: #2b2b2d;
    --paper: #ffffff;
    --brand-blue: #3ea3dc;
    --band-blue: #2f86cb;
    --ink-grey: #646464;
    --ink-white: #ffffff;
  }
  * { margin: 0; padding: 0; box-sizing: border-box; }
  html, body {
    width: 1200px; height: 800px; overflow: hidden;
    background: var(--backdrop);
    font-family: "Montserrat", "Helvetica Neue", Arial, sans-serif;
  }
  .canvas { position: relative; width: 1200px; height: 800px; }

  .card {
    position: absolute; top: 235px;
    width: 540px; height: 330px;
    overflow: hidden;
    box-shadow: 0 10px 30px rgba(0,0,0,.45);
  }
  .card--front { left: 40px; background: var(--paper); color: var(--ink-grey); }
  .card--back  { left: 620px; background: var(--brand-blue); color: var(--ink-white); }

  .brand-row { display: flex; align-items: center; gap: 12px; }
  .brand-square { flex: none; }

  /* front */
  .front-brand {
    position: absolute; right: 40px; top: 44px;
    display: flex; flex-direction: column; align-items: flex-end;
  }
  .front-brand .brand-square { width: 34px; height: 34px; background: var(--brand-blue); }
  .front-brand .brand-name { font-size: 38px; font-weight: 400; line-height: 1; color: var(--ink-grey); }
  .front-brand .brand-tagline { margin-top: 6px; font-size: 13px; font-weight: 300; color: var(--brand-blue); }
  .front-brand .brand-web { margin-top: 2px; font-size: 18px; font-weight: 300; letter-spacing: .3px; }

  .contact { position: absolute; left: 38px; top: 182px; }
  .contact-name { font-size: 22px; font-weight: 300; margin-bottom: 8px; }
  .contact-line { font-size: 13.5px; font-weight: 300; line-height: 1.6; }

  /* back */
  .back-brand {
    position: absolute; left: 44px; top: 40px;
    display: flex; flex-direction: column; align-items: flex-end;
  }
  .back-brand .brand-row { gap: 22px; }
  .back-brand .brand-square { width: 70px; height: 70px; background: var(--ink-white); }
  .back-brand .brand-name { font-size: 64px; font-weight: 400; line-height: 1; }
  .back-brand .brand-tagline { margin-top: 8px; font-size: 20px; font-weight: 300; }

  .module-band {
    position: absolute; left: 36px; right: 36px; bottom: 34px; height: 92px;
    background: var(--band-blue);
    display: flex; justify-content: space-around; align-items: center;
  }
  .module { display: flex; flex-direction: column; align-items: center; gap: 8px; }
  .module svg { width: 34px; height: 34px; }
  .module-label { font-size: 11px; font-weight: 600; }
</style>
</head>
<body>
<div class="canvas">

  <section class="card card--front" aria-label="Business card front">
    <div class="front-brand">
      <div class="brand-row">
        <span class="brand-square"></span>
        <span class="brand-name">zelVon</span>
      </div>
      <p class="brand-tagline">rewards that travel</p>
      <p class="brand-web">www.zelvon.example</p>
    </div>
    <div class="contact">
      <p class="contact-name">Carla Mendoza | Marketing</p>
      <p class="contact-line">W: www.zelvonapp.example</p>
      <p class="contact-line">M: + 61 400555123 | T: +61 2 5550 1473</p>
      <p class="contact-line">A: Suite 7, Level 2, 14-18 Harwick Street, Sydney NSW 2000</p>
    </div>
  </section>

  <section class="card card--back" aria-label="Business card back">
    <div class="back-brand">
      <div class="brand-row">
        <span class="brand-square"></span>
        <span class="brand-name">zelVon</span>
      </div>
      <p class="brand-tagline">rewards that travel</p>
    </div>

    <div class="module-band">
      <div class="module">
        <svg viewBox="0 0 34 34" fill="none" stroke="#fff" stroke-width="2.5" aria-hidden="true">
          <path d="M8 12 A11 11 0 0 1 26 9" /><path d="M26 22 A11 11 0 0 1 8 25" />
          <path d="M24 5 L27 9 L22 11" /><path d="M10 29 L7 25 L12 23" />
          <circle cx="17" cy="17" r="6" fill="#fff" stroke="none"/>
          <text x="17" y="21" font-size="10" text-anchor="middle" fill="#2f86cb" stroke="none" font-family="Arial, sans-serif" font-weight="700">$</text>
        </svg>
        <span class="module-label">CashBack Rewards</span>
      </div>
      <div class="module">
        <svg viewBox="0 0 34 34" fill="none" stroke="#fff" stroke-width="2.5" aria-hidden="true">
          <rect x="3" y="9" width="28" height="19" rx="3"/>
          <path d="M11 9 L13 5 H21 L23 9"/>
          <circle cx="17" cy="18.5" r="5.5"/>
        </svg>
        <span class="module-label">Tours &amp; Activities</span>
      </div>
      <div class="module">
        <svg viewBox="0 0 34 34" fill="none" stroke="#fff" stroke-width="2.5" stroke-linecap="round" aria-hidden="true">
          <path d="M7 4 V11 M10 4 V11 M13 4 V11 M7 11 Q10 15 13 11 M10 13 L25 30"/>
          <ellipse cx="24" cy="8" rx="4" ry="5" fill="#fff"/>
          <path d="M22 12 L9 30"/>
        </svg>
        <span class="module-label">Mobile Ordering</span>
      </div>
      <div class="module">
        <svg viewBox="0 0 34 34" aria-hidden="true">
          <path d="M4 12 L14 5 H30 V19 H14 Z" fill="#fff" transform="rotate(25 17 17)"/>
          <circle cx="12" cy="10" r="2" fill="#2f86cb"/>
        </svg>
        <span class="module-label">Local Offers</span>
      </div>
    </div>
  </section>

</div>
</body>
</html>
```